Website Banner Design Needed for Health/Medical Business

We are looking for a creative and professional set of banners for the front page of our:
1. website - tressrenewalnow.com.au and glowskinlab.com.au and bluemeadowco.com.au

then edit the above banners to the corrrect sizes for below
2. Our facebook pages (1 for each of the above websites)

3. Our google + pages (2 in total one for melb and syd)

4. You tube pages (1 for tressrenewalnow and 1 for glowskinlab)

We are looking for something fresh and clean that gives the feeling of:
1. Medical (dont show pictures of doctors though - nurses are ok - just not doctors)
2. Modern because PRP is a modern medical procedure
3. Most Experienced - No other clinic in Australia has performed as many PRP treatments compared to us.
4. We offer a 100% money back guarantee as well

The banners will not be animated or using layers. they will be still banners.

We would prefer to use new stock images and will purchase them for you after you have provided some suggestions/initial drafts.

Target Market(s)

men and women from 25-65

Industry/Entity Type

Health And Wellness

Number of Pages Required

1 page

Font styles to use
Sans Serif

Requirements
Must have
• no doctor images
• nurses are ok - but no doctor images
• for the images avoid fake themed images eg. a person looking in the mirror at their hair loss = NO NO NO..... instead aim for a nurse holding a test tube or a clipboard .
• The banners need to emphasise we are the only clinic who has performed 11,000+ treatments in australia
Nice to have
• a medical feeling would be nice - but dont make it too medical. i want the viewer to associate the word TRUSTED PROVEN and RELIABLE when they view the banner.
Should not have
• as mentioned no doctor or images that look like hospital too much.
• we are a private clinic run by nurses - i have to becareful not to mislead the viewer

```html
<!DOCTYPE html>
<html lang="en">
<head>
<meta charset="utf-8">
<title>PRP Hair Loss Treatments Banner</title>
<link rel="stylesheet" href="https://fonts.googleapis.com/css2?family=Oswald:wght@500&family=Tinos&family=Archivo+Black&display=swap">
<style>
  :root {
    --brand-blue: #2443b4;
    --sky-deep: #1e4cc2;
    --sky-mid: #3f8fe0;
    --sky-light: #cfe9fb;
    --ring-blue: #7ccbee;
    --hex-light: #b9dcf3;
    --hex-violet: #8e9ee0;
    --ink: #111111;
    --shadow-grey: #cfd3d8;
    --paper: #ffffff;
  }
  * { margin: 0; padding: 0; box-sizing: border-box; }
  html, body { width: 1200px; height: 389px; overflow: hidden; background: var(--paper); }
  .banner { position: relative; width: 1200px; height: 389px; overflow: hidden; background: var(--paper); }
  .banner-backdrop { position: absolute; inset: 0; }
  .nurse-photo {
    position: absolute; left: 0; top: 40px; width: 332px; height: 349px;
    background: linear-gradient(180deg, rgba(235,240,248,0) 0%, rgba(120,170,230,0.55) 35%, rgba(40,120,210,0.75) 100%);
    border-radius: 140px 140px 0 0;
  }
  .headline { position: absolute; inset: 0; color: var(--ink); }
  .headline-line {
    position: absolute; display: flex; align-items: baseline;
    white-space: nowrap; line-height: 1;
  }
  .headline-top { left: 330px; top: 122px; }
  .headline-bottom { left: 332px; top: 286px; }
  .accent-word {
    font-family: 'Oswald', sans-serif; font-weight: 500; color: var(--brand-blue);
  }
  .accent-word.only { font-size: 56px; letter-spacing: 2px; margin-right: 12px; }
  .accent-word.country { font-size: 31px; letter-spacing: 1px; margin-left: 14px; }
  .serif-line { font-family: 'Tinos', serif; color: var(--ink); }
  .headline-top .serif-line { font-size: 28px; }
  .headline-bottom .serif-line { font-size: 24px; }
  .treatment-count {
    position: absolute; left: 378px; top: 193px; white-space: nowrap;
    font-family: 'Archivo Black', sans-serif; font-size: 88px; line-height: 1;
    letter-spacing: -4px; color: var(--ink);
    text-shadow: -6px -3px 0 var(--shadow-grey);
  }
  .result-circle {
    position: absolute; width: 168px; height: 168px; border-radius: 50%;
    border: 8px solid var(--ring-blue); background: var(--paper); padding: 4px;
  }
  .result-photo {
    width: 100%; height: 100%; border-radius: 50%;
    background: linear-gradient(180deg, #0c0c0c 0 16%, #8d8d8d 16% 50%, #3a3a3a 50% 84%, #0c0c0c 84%);
  }
  .result-top { left: 894px; top: 50px; }
  .result-left { left: 806px; top: 206px; }
  .result-right { left: 978px; top: 206px; }
</style>
</head>
<body>
<div class="banner">
  <svg class="banner-backdrop" width="1200" height="389" viewBox="0 0 1200 389" aria-hidden="true">
    <defs>
      <linearGradient id="top-wave" x1="0" y1="0" x2="1" y2="0">
        <stop offset="0" stop-color="#5fa9ea"/>
        <stop offset="0.5" stop-color="#3f8fe0"/>
        <stop offset="1" stop-color="#1e4cc2"/>
      </linearGradient>
      <linearGradient id="bottom-wave" x1="0" y1="0" x2="1" y2="0">
        <stop offset="0" stop-color="#9fd2f5"/>
        <stop offset="1" stop-color="#c9e6fa"/>
      </linearGradient>
    </defs>
    <path d="M0 0 H1200 V18 C900 40 500 30 0 60 Z" fill="url(#top-wave)"/>
    <path d="M0 60 C400 34 800 40 1200 18 V34 C820 50 420 60 0 88 Z" fill="#cfe9fb" opacity="0.7"/>
    <circle cx="864" cy="84" r="100" fill="#eef5fc"/>
    <path d="M0 372 C400 356 800 358 1200 352 V389 H0 Z" fill="url(#bottom-wave)"/>
    <polygon points="676,278 702,278 715,300 702,322 676,322 663,300" fill="#b9dcf3" opacity="0.8"/>
    <polygon points="705,296 733,296 747,320 733,344 705,344 691,320" fill="#b9dcf3" opacity="0.6"/>
    <polygon points="718,328 746,328 760,352 746,376 718,376 704,352" fill="#8e9ee0"/>
  </svg>

  <div class="nurse-photo" role="img" aria-label="Smiling nurse in blue scrubs with a stethoscope, holding a tablet"></div>

  <div class="headline">
    <p class="headline-line headline-top"><span class="accent-word only">ONLY</span><span class="serif-line">clinic to perform</span></p>
    <p class="treatment-count">11000+</p>
    <p class="headline-line headline-bottom"><span class="serif-line">prp for hair loss treatments in</span><span class="accent-word country">AUSTRALIA</span></p>
  </div>

  <div class="result-circle result-top"><div class="result-photo" role="img" aria-label="Before and after photo of a man's hairline"></div></div>
  <div class="result-circle result-left"><div class="result-photo" role="img" aria-label="Before and after photo of a thinning crown"></div></div>
  <div class="result-circle result-right"><div class="result-photo" role="img" aria-label="Before and after photo of the back of a man's head"></div></div>
</div>
</body>
</html>
```